To design a brand identity that is simple and creative with 'Valdor' as the brand name, I like modern simple fonts like helvetica neue, I want to print both sides of the card, I am open to dark front and white back, but the design needs to transfer well to letter heads and email signatures, I am looking for sophisticated and elegant, but open minded about clever and off the wall, I do not do 'boring' Valdor Holdings is the mother company for a small group, specialising in Management & consulting, Software development and construction, we have a high level of integrity, we are transparent and accountable for what we do. my images are provided as a guide only, Im not expecting them to be just copied, Im looking for a creator and passionate thinker, who will put life into their work.

Target Market(s)

usually business minded people who are looking for something different in me, such as leadership, confidence and focus with thinking that is per haps a little outside the box..

Industry/Entity Type

Construction

Requirements
Must have
• clean, minmalistic
Nice to have
• custom logo
Should not have
• boring, traditional

```html
<!DOCTYPE html>
<html lang="en">
<head>
<meta charset="utf-8">
<title>Valdor — Business Card</title>
<link rel="stylesheet" href="https://fonts.googleapis.com/css2?family=Nunito:wght@300;400;700&family=Cormorant+Garamond:ital,wght@1,500&display=swap">
<style>
  :root {
    --page: #ffffff;
    --card: #000000;
    --brand-orange: #e2692f;
    --accent-red: #e8553a;
    --tagline: #f2f2f2;
    --mark: #e2692f;
  }
  * { margin: 0; padding: 0; box-sizing: border-box; }
  html, body {
    width: 1200px;
    height: 503px;
    overflow: hidden;
    background: var(--page);
  }
  .canvas {
    position: relative;
    width: 1200px;
    height: 503px;
  }
  .card {
    position: absolute;
    width: 430px;
    height: 269px;
    background: var(--card);
  }
  .card--front { left: 111px; top: 114px; }
  .card--back  { left: 663px; top: 118px; }

  .brand {
    position: absolute;
    display: flex;
    align-items: center;
  }
  .brand__dot {
    border-radius: 50%;
    background: var(--mark);
    flex: none;
  }
  .brand__name {
    font-family: "Nunito", sans-serif;
    font-weight: 300;
    color: var(--brand-orange);
    line-height: 1;
  }
  .brand__tagline {
    position: absolute;
    font-family: "Cormorant Garamond", serif;
    font-style: italic;
    font-weight: 500;
    color: var(--tagline);
    white-space: nowrap;
  }

  /* front */
  .card--front .brand { left: 42px; top: 88px; gap: 22px; }
  .card--front .brand__dot { width: 58px; height: 58px; }
  .card--front .brand__name { font-size: 66px; letter-spacing: 1px; }
  .card--front .brand__tagline { right: 55px; top: 181px; font-size: 16px; }

  /* back */
  .card--back .brand { left: 42px; top: 109px; gap: 8px; }
  .card--back .brand__dot { width: 22px; height: 22px; }
  .card--back .brand__name { font-size: 25px; }
  .card--back .brand__tagline { left: 98px; top: 135px; font-size: 6px; }

  .divider {
    position: absolute;
    left: 208px;
    top: 73px;
    width: 1.5px;
    height: 125px;
    background: var(--brand-orange);
  }
  .contact {
    position: absolute;
    right: 35px;
    top: 99px;
    text-align: right;
    font-family: "Nunito", sans-serif;
    color: var(--accent-red);
    font-size: 13px;
    line-height: 1.25;
  }
  .contact__email { font-weight: 700; font-size: 15px; }
  .contact__role { font-weight: 400; margin-bottom: 12px; }
  .contact__phone { margin-bottom: 4px; }
  .services {
    position: absolute;
    left: 0;
    right: 0;
    top: 216px;
    text-align: center;
    font-family: "Nunito", sans-serif;
    font-weight: 400;
    font-size: 18px;
    color: var(--accent-red);
    letter-spacing: 0.3px;
  }
</style>
</head>
<body>
<main class="canvas">
  <section class="card card--front">
    <div class="brand">
      <span class="brand__dot"></span>
      <span class="brand__name">valdor</span>
    </div>
    <p class="brand__tagline">..shaping what comes next.</p>
  </section>

  <section class="card card--back">
    <div class="brand">
      <span class="brand__dot"></span>
      <span class="brand__name">valdor</span>
    </div>
    <p class="brand__tagline">..shaping what comes next.</p>
    <span class="divider"></span>
    <div class="contact">
      <p class="contact__email">owen@valdor.holdings</p>
      <p class="contact__role">Client Ambassador</p>
      <p class="contact__phone">+61 040 552 914</p>
      <p class="contact__address">Po Box 418 Perth 6000</p>
    </div>
    <p class="services">Management, software, construction</p>
  </section>
</main>
</body>
</html>
```